KVTR Marketing Flyers

We would like to make 5 x A4 marketing flyers that we can hand to our customers. We are an engineering company based in Australia.
We make a machine called a Kelvar Vane Trestle Rig (KVTR).
The first flyer we would like to do is give an overview of the KVTR which can be made in 4 different designs.
Then we would like to make a flyer for each design. The 4 different designs are:
Compressor KVTR
Multipurpose KVTR
Rod Storage KVTR
Container KVTR
I have attached images for each desgin as well as the text we require. Our website is www.morrowvaleengineering.com.au for you to look at our colours etc and get a feel for our business. We want the flyer to be modern and clean but classy.
The Morrowvale Engineering KVTR - this is the text for the overview flyer

```html
<!DOCTYPE html>
<html lang="en">
<head>
<meta charset="utf-8">
<title>KVTR Flyers</title>
<link href="https://fonts.googleapis.com/css2?family=Poppins:ital,wght@0,400;0,500;0,600;0,700;1,400;1,500&display=swap" rel="stylesheet">
<style>
:root{
  --board:#333335;
  --navy:#27398f;
  --blue:#3350b0;
  --green:#1aa049;
  --green-light:#2dbb5a;
  --sky:#d3e2f4;
  --ink:#3d3d3d;
  --white:#ffffff;
}
*{box-sizing:border-box;margin:0;padding:0}
html,body{width:1200px;height:864px;overflow:hidden}
body{background:var(--board);font-family:'Poppins',sans-serif;color:var(--ink);position:relative}
.board-label{position:absolute;top:38px;color:var(--white);font-weight:600;font-size:21px;transform:translateX(-50%);white-space:nowrap}
.page{position:absolute;top:76px;width:518px;height:730px;background:var(--white);overflow:hidden}
.page--overview{left:74px}
.page--single{left:622px}

/* overview */
.section-tab{position:absolute;height:40px;width:183px;border-radius:4px;color:var(--white);font-size:11.5px;font-weight:500;line-height:13px;display:flex;align-items:center;padding-left:19px}
.section-tab--blue{background:linear-gradient(90deg,var(--navy),var(--blue))}
.section-tab--green{background:linear-gradient(90deg,#18914a,var(--green-light))}
.tab-tick{position:absolute;left:-8px;top:12px;width:17px;height:17px;border-radius:50%;border:1.5px solid var(--white)}
.tab-tick--green{background:var(--green)}
.tab-tick--blue{background:var(--navy)}
.tab-tick::after{content:"";position:absolute;left:4.5px;top:2.5px;width:4px;height:7px;border:solid var(--white);border-width:0 1.6px 1.6px 0;transform:rotate(45deg)}
.section-copy{position:absolute;font-size:7.7px;line-height:9.6px;color:var(--ink)}
.section-copy p{margin-bottom:5px}
.section-copy .lead-in{color:var(--navy);font-style:italic;font-weight:500;margin-bottom:4px}
.ticks{list-style:none}
.ticks li{position:relative;padding-left:11px}
.ticks li::before{content:"";position:absolute;left:1px;top:2px;width:6px;height:6px;border-radius:50%;background:var(--green)}
.ticks li::after{content:"";position:absolute;left:3.2px;top:3px;width:1.4px;height:2.6px;border:solid var(--white);border-width:0 1px 1px 0;transform:rotate(45deg)}
.render-frame{position:absolute;border:1px solid var(--green);padding:6px;background:var(--white)}
.render-fill{width:100%;height:100%;border-radius:2px}
.tagline{position:absolute;left:20px;right:20px;top:642px;text-align:center;color:var(--navy);font-size:10.6px;line-height:12.6px}
.tagline strong{font-weight:600}
.contact-bar{position:absolute;left:0;right:0;top:692px;height:38px;border-top:1px solid var(--navy);display:flex;align-items:center;justify-content:space-between;padding:0 14px 0 24px;font-size:9.6px;color:#2a2a2a}
.contact-item{display:flex;align-items:center;gap:3px;white-space:nowrap}
.contact-item svg{width:9px;height:9px}

/* single design flyer */
.flyer-art{position:absolute;left:0;top:0;width:518px;height:730px}
.brand-name{position:absolute;left:24px;top:20px;color:var(--navy);font-weight:700;font-size:21px;line-height:23px;display:flex;align-items:center;gap:8px}
.brand-mark{width:12px;height:12px;border-radius:50%;background:var(--navy);flex:none}
.flyer-title{position:absolute;right:22px;top:18px;text-align:right;font-weight:700;font-size:29.5px;line-height:32px;color:var(--navy)}
.flyer-title .accent{color:var(--green)}
.title-rule{position:absolute;top:125px;left:354px;width:138px;height:2px;background:linear-gradient(90deg,var(--navy) 78%,var(--green) 78%)}
.flyer-intro{position:absolute;left:41px;top:453px;width:350px;font-size:12.4px;line-height:14px;color:#333}
.flyer-intro strong{color:var(--navy);font-weight:600}
.flyer-subhead{position:absolute;left:40px;top:542px;color:var(--green);font-weight:600;font-size:11.4px}
.flyer-features{position:absolute;top:567px;font-size:10.6px;line-height:12.7px;color:#333}
.flyer-features li{padding-left:14px;margin-bottom:6px}
.flyer-features li::before{width:8px;height:8px;top:2.5px}
.flyer-features li::after{left:3.9px;top:3.6px;width:1.8px;height:3.4px}
</style>
</head>
<body>

<div class="board-label" style="left:343px">back page 1</div>
<div class="board-label" style="left:880px">FLyer 3</div>

<section class="page page--overview">
  <div class="section-tab section-tab--blue" style="left:36px;top:32px"><span class="tab-tick tab-tick--green"></span>Multipurpose Kelvar Vane Trestle Rig</div>
  <div class="section-copy" style="left:35px;top:82px;width:228px">
    <p>The multipurpose Kelvar Vane Trestle Rig is a versatile option designed for various applications, featuring a standard flat deck that allows for easy mounting of different equipment configurations. Some of the different configurations we have designed are;</p>
    <ul class="ticks">
      <li>15000L water tank</li>
      <li>12000L Water tank</li>
      <li>12000L Water Tank and 3000L Diesel tank, 24v diesel pump</li>
      <li>Diamond rod sloop with folding doors 1 end and tilting door the other end</li>
      <li>10ft sea container workshop</li>
    </ul>
  </div>

  <div class="section-tab section-tab--green" style="left:278px;top:33px"><span class="tab-tick tab-tick--blue"></span>Compressor KVTR</div>
  <div class="section-copy" style="left:278px;top:85px;width:224px">
    <p>The Compressor Kelvar Vane Trestle Rig is tailored to accommodate compressors used in drilling operations, with jack legs positioned strategically to fit larger compressors between them. Its compact size allows for multiple bases to be transported on a single trailer for convenience during mobilisation.</p>
    <p class="lead-in">Some of the benefits of the Compressor KVTR are;</p>
    <ul class="ticks">
      <li>Legs are as far apart as possible to allow the bigger compressors to fit.</li>
      <li>Size of the base is the same as a 20ft Sea Container, multiple bases can fit on a 40ft trailer.</li>
      <li>Leg positioning allows all the doors to be opened for ease of maintenance while at ground level.</li>
    </ul>
  </div>

  <div class="section-tab section-tab--green" style="left:36px;top:233px"><span class="tab-tick tab-tick--blue"></span>Pipe Storage KVTR</div>
  <div class="section-copy" style="left:35px;top:284px;width:228px">
    <p>The pipe storage Kelvar vane trestle rig is designed where drill pipes or casing can be stored on the base. This design has tilting legs to allow the rods to be picked up from the one side, without lifting them over the legs. The features of this design are;</p>
    <ul class="ticks">
      <li>The overall length of the base is 6.5m, to allow storage of drill pipes / casing.</li>
      <li>Fold down headboard on one end to allow for easier loading / unloading.</li>
      <li>The legs fold down on one side to allow access without lifting the pipes or casing over the legs.</li>
    </ul>
  </div>

  <div class="section-tab section-tab--blue" style="left:278px;top:234px"><span class="tab-tick tab-tick--green"></span>Container KVTR</div>
  <div class="section-copy" style="left:278px;top:287px;width:224px">
    <p>The Container Kelvar Vane Trestle Rig is designed with a longer frame to accommodate a standard 20ft sea container between the legs. With a clearance between the legs of 6.5m, this design also works for pipe storage and handling if it is a requirement to manoeuvre the pipes between the legs. Some of the setups we have completed with this design are;</p>
    <ul class="ticks">
      <li>Standard 20ft sea container mounted on the base</li>
      <li>Standard 20ft container, split in 2 with one end being a workshop, and one being an air-conditioned office.</li>
      <li>Rod handling sloop, operating with a freedom loader, where the pipes are passed between the legs.</li>
    </ul>
  </div>

  <div class="render-frame" style="left:40px;top:440px;width:221px;height:96px">
    <div class="render-fill" role="img" aria-label="3D render of the multipurpose rig carrying a white water tank on a yellow frame" style="background:linear-gradient(135deg,#fbf6d8,#f4e46a 55%,#eef0f0)"></div>
  </div>
  <div class="render-frame" style="left:270px;top:440px;width:217px;height:96px">
    <div class="render-fill" role="img" aria-label="3D render of the compressor rig carrying two cream compressors on a yellow frame" style="background:linear-gradient(135deg,#f6f3e2,#e8e3c4 55%,#c9c7b9)"></div>
  </div>
  <div class="render-frame" style="left:40px;top:544px;width:141px;height:89px">
    <div class="render-fill" role="img" aria-label="3D render of the empty yellow rig frame with jack legs" style="background:linear-gradient(135deg,#fbf6d8,#f3df52 60%,#f7f3dc)"></div>
  </div>
  <div class="render-frame" style="left:193px;top:544px;width:141px;height:89px">
    <div class="render-fill" role="img" aria-label="3D render of the container rig carrying an orange sea container" style="background:linear-gradient(135deg,#f8e7d8,#d9773a 55%,#f1e7b2)"></div>
  </div>
  <div class="render-frame" style="left:345px;top:544px;width:141px;height:89px">
    <div class="render-fill" role="img" aria-label="3D render of the blue pipe storage rig loaded with pipes" style="background:linear-gradient(135deg,#e8eef8,#6e9ad4 55%,#e6ebf0)"></div>
  </div>

  <p class="tagline">Discover the <strong>versatility</strong> and <strong>sustainability</strong> of the <strong>Morrowvale Engineering<br>Kelvar Vane Trestle Rig range,</strong> offering innovative solutions for mining operations<br>while prioritizing environmental responsibility</p>

  <div class="contact-bar">
    <span class="contact-item"><svg viewBox="0 0 10 10"><path d="M2 1l2 2-1 1.2c.6 1.2 1.5 2.1 2.8 2.8L7 6l2 2-1.3 1.2C4.5 9 1 5.5.8 2.3z" fill="none" stroke="#1aa049" stroke-width=".8"/></svg>+61 400 555 019</span>
    <span class="contact-item"><svg viewBox="0 0 10 10"><path d="M5 9.5S1.8 6 1.8 3.8a3.2 3.2 0 016.4 0C8.2 6 5 9.5 5 9.5z" fill="#1aa049"/><circle cx="5" cy="3.8" r="1.2" fill="#fff"/></svg>48 Carrow St, Halden 6099</span>
    <span class="contact-item"><svg viewBox="0 0 10 10"><rect x=".7" y="2" width="8.6" height="6" fill="none" stroke="#1aa049" stroke-width=".8"/><path d="M.7 2L5 5.5 9.3 2" fill="none" stroke="#1aa049" stroke-width=".8"/></svg>info@morrowvaleengineering.com.au</span>
  </div>
</section>

<section class="page page--single">
  <svg class="flyer-art" viewBox="0 0 518 730" preserveAspectRatio="none">
    <defs>
      <linearGradient id="siteTones" x1="0" y1="0" x2="0" y2="1">
        <stop offset="0" stop-color="#cfdcea"/>
        <stop offset=".28" stop-color="#b9c2c4"/>
        <stop offset=".42" stop-color="#8d5a45"/>
        <stop offset=".55" stop-color="#3f62b4"/>
        <stop offset=".7" stop-color="#b7875a"/>
        <stop offset="1" stop-color="#c8a077"/>
      </linearGradient>
    </defs>
    <rect x="0" y="0" width="518" height="360" fill="#d3e2f4"/>
    <rect x="0" y="128" width="518" height="420" fill="url(#siteTones)" role="img" aria-label="Photograph of the blue pipe storage rig loaded with rusty drill pipes on a dirt yard"/>
    <path d="M0 0H264C236 80 140 112 0 120Z" fill="#ffffff"/>
    <path d="M0 120C140 112 236 80 264 0H273C252 100 150 132 0 143Z" fill="#27398f"/>
    <path d="M0 346C190 322 380 352 490 458C360 392 200 372 0 382Z" fill="#27398f"/>
    <path d="M0 382C200 372 360 392 490 458L517 470V532C430 440 240 385 0 392Z" fill="#ffffff"/>
    <path d="M0 392C240 385 430 440 517 470V532C430 446 240 398 0 398Z" fill="#1aa049"/>
    <path d="M0 398C240 398 430 446 517 532V730H0Z" fill="#ffffff"/>
    <line x1="0" y1="692" x2="518" y2="692" stroke="#27398f" stroke-width="1"/>
  </svg>

  <div class="brand-name"><span class="brand-mark"></span><span>MORROWVALE<br>ENGINEERING</span></div>

  <h1 class="flyer-title">Pipe Storage<br>Kelvar Vane<br><span class="accent">Trestle Rig</span></h1>
  <div class="title-rule"></div>

  <p class="flyer-intro"><strong>The pipe storage Kelvar vane</strong> trestle rig is designed where drill pipes or casing can be stored on the base. This design has tilting legs to allow the rods to be picked up from the one side, without lifting them over the legs. The features of this design are;</p>

  <h2 class="flyer-subhead">Our innovative designs include:</h2>
  <ul class="ticks flyer-features" style="left:40px;width:205px">
    <li>The overall length of the base is 6.5m, to allow storage of drill pipes / casing.</li>
    <li>Fold down headboard on one end to allow for easier loading / unloading.</li>
  </ul>
  <ul class="ticks flyer-features" style="left:256px;width:230px">
    <li>The legs fold down on one side to allow access without lifting the pipes or casing over the legs.</li>
  </ul>

  <div class="contact-bar" style="border-top:none">
    <span class="contact-item"><svg viewBox="0 0 10 10"><path d="M2 1l2 2-1 1.2c.6 1.2 1.5 2.1 2.8 2.8L7 6l2 2-1.3 1.2C4.5 9 1 5.5.8 2.3z" fill="none" stroke="#1aa049" stroke-width=".8"/></svg>+61 400 555 019</span>
    <span class="contact-item"><svg viewBox="0 0 10 10"><path d="M5 9.5S1.8 6 1.8 3.8a3.2 3.2 0 016.4 0C8.2 6 5 9.5 5 9.5z" fill="#1aa049"/><circle cx="5" cy="3.8" r="1.2" fill="#fff"/></svg>48 Carrow St, Halden 6099</span>
    <span class="contact-item"><svg viewBox="0 0 10 10"><rect x=".7" y="2" width="8.6" height="6" fill="none" stroke="#1aa049" stroke-width=".8"/><path d="M.7 2L5 5.5 9.3 2" fill="none" stroke="#1aa049" stroke-width=".8"/></svg>info@morrowvaleengineering.com.au</span>
  </div>
</section>

</body>
</html>
```